Website design for Harbor Bolts. ( Lock company)

Harbor Bolts is a New York Based Company that manufactures a variety of high quality Locks which sell worldwide.

Our website: We need a 'face' on the Internet , a website that tells you who we are and what we do - 'An Identity'.

it is not an eCommerce website . the website is to show customers and potential distributers who we are and what we manufacture ( so they come away with a great impression of our company and our products) see www.quarrelwheel.com

First glance impression: We are Professional; are locks are strong,and reliable. and we are ready to compete with other major Lock companies

Content: for starters the site will contain general information and background about our company (our story), were to buy our products, contact information, and display images of our Locks (and of course all the classic links including to all the legal and technical information). as time goes on we will add more features to the website i.e. Products, Videos blogs etc.

although at first there will not be that much content on the website - it should not look empty (it should be simple and clear but not empty) it should look and feel like a full fledged professional website (not a template)

Inspiration: here are a few sites which have the feel we are looking for:

General tone - quarrelwheel.com bramhold.com (black is good - But not a must )

Simplicity, clarity - coldvane.com panwright.com

the widescreen Image look - http://www.pagecritter.com/demo/58261.html

we are considering perhaps having wide HQ images of Lion(s) in the background (but without the felling that it is a zoo or safari website) - it is not a must, its just an idea .

perhaps (if you find it looks good ) use a bit of that metal or chrome look to give it it a strong smooth feel (however it should not look like a dark prison)

We do not currently have a Logo ( if you feel you can design one that fits the above company description - we would love to see if it can work for us) We can talk about additional funds for the logo during this project.

Our working slogan is : Harbor Bolts - "Keeper of your Ground"

for your convenience we have attached a few images of the type of locks we sell

We are looking to collaborate with you throughout the project. We have ideas and visions we want implemented and we will help you along the way. So we can create the perfect website.

Thank you.

```html
<!DOCTYPE html>
<html lang="en">
<head>
<meta charset="utf-8">
<title>Harbor Bolts - Keeper of your Ground</title>
<link href="https://fonts.googleapis.com/css2?family=Anton&family=Oswald:wght@500;600&family=Questrial&display=swap" rel="stylesheet">
<style>
  :root {
    --page: #1a1a1a;
    --panel: #0a0a0a;
    --card: #242424;
    --nav: #0e0e0e;
    --red: #ed1c24;
    --yellow: #fff200;
    --white: #ffffff;
    --muted: #b9b9b9;
    --line: #3a3a3a;
    --steel-light: #e9e9e9;
  }
  * { box-sizing: border-box; margin: 0; padding: 0; }
  html, body { width: 680px; height: 1200px; overflow: hidden; background: var(--page); }
  .site {
    position: relative; width: 680px; height: 1200px; overflow: hidden;
    background: linear-gradient(180deg, #1b1b1b 0%, #1a1a1a 75%, #241a14 100%);
    font-family: "Questrial", Arial, sans-serif; color: var(--white);
  }
  .abs { position: absolute; }

  /* Hero */
  .hero-photo {
    left: 0; top: 0; width: 680px; height: 376px;
    background:
      radial-gradient(ellipse 220px 260px at 560px 170px, #9a9a9a 0%, #5d5d5d 35%, #2a2a2a 70%, transparent 100%),
      linear-gradient(90deg, #111 0%, #1a1a1a 45%, #3a3a3a 100%);
  }
  .nav {
    left: 0; top: 0; width: 680px; height: 45px; background: rgba(10,10,10,0.85);
  }
  .nav a {
    position: absolute; top: 0; height: 45px; line-height: 45px;
    font-family: "Oswald", sans-serif; font-weight: 600; font-size: 10px;
    letter-spacing: 0.4px; color: var(--white); text-decoration: none;
    transform: translateX(-50%); white-space: nowrap;
  }
  .nav a.active { background: var(--red); width: 60px; text-align: center; }
  .hero-star { left: 331px; top: 105px; }
  .brand {
    left: 0; width: 680px; top: 140px; text-align: center;
    font-family: "Anton", sans-serif; font-size: 64px; line-height: 80px;
    color: var(--white); letter-spacing: 1px;
  }
  .tagline {
    left: 0; width: 680px; top: 230px; text-align: center;
    font-family: "Anton", sans-serif; font-size: 27px; color: var(--yellow);
  }
  .dots { left: 315px; top: 289px; display: flex; gap: 5px; }
  .dots span { width: 9px; height: 9px; border: 1.5px solid var(--white); border-radius: 50%; }
  .dots span.on { border-color: var(--red); }

  /* Promo */
  .promo { left: 74px; top: 324px; width: 532px; height: 112px; background: var(--panel); }
  .promo h2 {
    position: absolute; left: 18px; top: 18px;
    font-family: "Oswald", sans-serif; font-weight: 600; font-size: 12px;
  }
  .promo h2 em { font-style: normal; color: var(--red); }
  .promo p {
    position: absolute; left: 18px; top: 44px; width: 320px;
    font-size: 6.4px; line-height: 12px; text-transform: uppercase; color: #ddd;
  }
  .btn-more {
    position: absolute; left: 19px; top: 76px; width: 58px; height: 21px;
    background: #333; border-radius: 3px; font-size: 7px; line-height: 21px;
    text-align: center; color: var(--white);
  }
  .promo-photo {
    position: absolute; right: 0; top: 0; width: 200px; height: 112px;
    background: radial-gradient(ellipse at 55% 55%, #d9b260 0%, #9b7a36 40%, #2a2a2a 80%, #0a0a0a 100%);
  }

  /* Sections */
  .section-title {
    left: 0; width: 680px; text-align: center;
    font-family: "Anton", sans-serif; font-size: 19px; letter-spacing: 0.3px;
  }
  .section-title em { font-style: normal; color: var(--red); }
  .section-text {
    left: 80px; width: 520px; text-align: center;
    font-size: 7.6px; line-height: 11.2px; color: var(--muted);
  }

  /* Product cards */
  .card { top: 546px; width: 119px; height: 196px; background: var(--card); }
  .card .photo { height: 97px; background: radial-gradient(circle at 50% 50%, #bfbfbf 0%, #efefef 55%); }
  .card h3 {
    margin-top: 13px; text-align: center;
    font-family: "Oswald", sans-serif; font-weight: 600; font-size: 10.5px;
  }
  .card p {
    margin: 10px 8px 0; text-align: center; font-size: 6.4px; line-height: 9px; color: var(--muted);
  }
  .card .read {
    position: absolute; left: 0; bottom: 0; width: 119px; height: 21px; background: var(--red);
    text-align: center; line-height: 21px; font-size: 8px; color: var(--white);
  }
  .card .read::before {
    content: ""; position: absolute; left: 56px; top: -4px;
    border-left: 4px solid transparent; border-right: 4px solid transparent; border-bottom: 4px solid var(--red);
  }
  .divider { left: 74px; top: 768px; width: 532px; height: 1px; background: var(--line); }

  /* Offer */
  .offer {
    left: 74px; top: 854px; width: 532px; height: 128px;
    background: radial-gradient(ellipse at 60% 50%, #2a1512 0%, #120b0a 60%, #0a0808 100%);
  }
  .offer-frame { position: absolute; left: 6px; top: 6px; right: 6px; bottom: 6px; border: 1.5px solid #3d3432; }
  .offer-photo {
    position: absolute; left: 30px; top: 18px; width: 80px; height: 88px;
    background: linear-gradient(180deg, #bdbdbd 0%, #8e9aa5 60%, #2c3d8a 100%); border-radius: 8px 8px 4px 4px; opacity: 0.9;
  }
  .offer-kicker {
    position: absolute; left: 144px; top: 40px;
    font-family: "Anton", sans-serif; font-size: 20px; line-height: 24px; color: var(--red);
  }
  .offer-sub {
    position: absolute; left: 144px; top: 66px;
    font-family: "Anton", sans-serif; font-size: 20px; line-height: 24px; color: var(--white);
  }
  .offer-deal {
    position: absolute; left: 340px; top: 36px;
    font-family: "Anton", sans-serif; font-size: 44px; line-height: 56px; color: var(--white);
  }

  /* Bottom boxes */
  .box { top: 1011px; width: 255px; height: 98px; background: var(--panel); }
  .box h4 {
    position: absolute; left: 15px; top: 16px;
    font-family: "Anton", sans-serif; font-size: 18px; letter-spacing: 0.3px;
  }
  .box p { position: absolute; left: 18px; top: 51px; width: 225px; font-size: 7.6px; line-height: 10.6px; color: #ddd; }
  .box p b { font-weight: 400; color: var(--red); margin-left: 12px; }
  .email {
    position: absolute; left: 19px; top: 47px; width: 178px; height: 29px;
    border: 1px solid #444; font-size: 7.6px; line-height: 27px; padding-left: 8px; color: #ccc;
  }
  .go {
    position: absolute; left: 196px; top: 47px; width: 37px; height: 29px; background: var(--red);
    font-family: "Anton", sans-serif; font-size: 14px; line-height: 29px; text-align: center;
  }

  /* Footer */
  .footer-line { left: 74px; top: 1134px; width: 532px; height: 1px; background: var(--line); }
  .footer-nav {
    left: 74px; top: 1150px; display: flex; gap: 7px;
    font-family: "Oswald", sans-serif; font-weight: 600; font-size: 7.6px; color: #cfcfcf;
  }
  .footer-legal { left: 74px; top: 1173px; display: flex; gap: 7px; font-size: 7px; color: #b0b0b0; }
  .social { left: 478px; top: 1150px; display: flex; gap: 5px; }
  .social span { width: 21px; height: 21px; }
</style>
</head>
<body>
<div class="site">

  <div class="abs hero-photo" role="img" aria-label="Wide black and white photograph of a lion resting on the right side of the hero"></div>

  <nav class="abs nav">
    <a class="active" href="#" style="left:104px">HOME</a>
    <a href="#" style="left:177px">ABOUT US</a>
    <a href="#" style="left:258px">SERVICES</a>
    <a href="#" style="left:336px">GALLERY</a>
    <a href="#" style="left:406px">BLOG</a>
    <a href="#" style="left:487px">TESTIMONIALS</a>
    <a href="#" style="left:582px">CONTACT US</a>
  </nav>

  <svg class="abs hero-star" width="18" height="18" viewBox="0 0 24 24" aria-hidden="true">
    <polygon points="12,1 15,9 23.5,9 16.7,14 19.3,22.5 12,17.3 4.7,22.5 7.3,14 0.5,9 9,9" fill="#fff"/>
  </svg>
  <h1 class="abs brand">HARBOR BOLTS</h1>
  <div class="abs tagline">KEEPER OF YOUR GROUND</div>
  <div class="abs dots"><span></span><span class="on"></span><span></span><span></span></div>

  <section class="abs promo">
    <h2>NEQUE <em>SMART SECURITY</em> QUI DOLOREM IPSUM QUIA DOLOR SIT.</h2>
    <p>Sed ut perspiciatis unde omnis iste natus error sit voluptatem accusantium doloremque laudantium, totam rem aperiam, eaque ipsa quae ab illo inventore veritatis ...</p>
    <div class="btn-more">VIEW MORE</div>
    <div class="promo-photo" role="img" aria-label="Photograph of a brass door knob lock set with key"></div>
  </section>

  <h2 class="abs section-title" style="top:455px">WELCOME TO OUR HARBOR BOLTS</h2>
  <p class="abs section-text" style="top:492px">Sed ut perspiciatis unde omnis iste natus error sit voluptatem accusantium doloremque laudantium, totam rem aperiam, eaque ipsa quae ab illo inventore veritatis et quasi architecto beatae vitae dicta sunt explicabo. Nemo enimSed ut perspiciatis unde omnis iste natus error sitklhcgh voluptaccusantium doloremque laudantium, totam rem aperiam, eaque ipsa quae ab illo inventore veritatis et quasi architecto beatae</p>

  <article class="abs card" style="left:74px">
    <div class="photo" role="img" aria-label="Photograph of a black combination key safe padlock"></div>
    <h3>QUISQUAMEST QUI</h3>
    <p>Sed ut perspiciatis unde omni iste natus error sit voluptatem lou accusantium doloremque</p>
    <div class="read">READ MORE</div>
  </article>
  <article class="abs card" style="left:214px">
    <div class="photo" role="img" aria-label="Photograph of a laminated steel padlock with key"></div>
    <h3>QUISQUAMEST QUI</h3>
    <p>Sed ut perspiciatis unde omni iste natus error sit voluptatem lou accusantium doloremque</p>
    <div class="read">READ MORE</div>
  </article>
  <article class="abs card" style="left:347px">
    <div class="photo" role="img" aria-label="Photograph of a brass deadbolt lock with key"></div>
    <h3>QUISQUAMEST QUI</h3>
    <p>Sed ut perspiciatis unde omni iste natus error sit voluptatem lou accusantium doloremque</p>
    <div class="read">READ MORE</div>
  </article>
  <article class="abs card" style="left:487px">
    <div class="photo" role="img" aria-label="Photograph of a long shackle steel padlock with keys"></div>
    <h3>QUISQUAMEST QUI</h3>
    <p>Sed ut perspiciatis unde omni iste natus error sit voluptatem lou accusantium doloremque</p>
    <div class="read">READ MORE</div>
  </article>

  <div class="abs divider"></div>

  <h2 class="abs section-title" style="top:785px">FEATURES &amp; <em>O</em>FFERS</h2>
  <p class="abs section-text" style="top:817px">Sed ut perspiciatis unde omnis iste natus error sit voluptatem accusantium doloremque laudantium, totam rem aperiam, eaque ipsa quae ab illo inventore veritatis et quasi architecto beatae vitae dicta sunt explicabo. Nemo enimSed ut perspiciatis unde omnis iste natus error sitklhcgh</p>

  <section class="abs offer">
    <div class="offer-frame"></div>
    <div class="offer-photo" role="img" aria-label="Photograph of a steel padlock with key"></div>
    <div class="offer-kicker">ELECTRONIC LOCKS</div>
    <div class="offer-sub">QUI DOLOREM IPSUM</div>
    <div class="offer-deal">45% OFF</div>
  </section>

  <section class="abs box" style="left:74px">
    <h4>TESTIMONILAS <svg width="8" height="10" viewBox="0 0 8 10" style="margin-left:6px" aria-hidden="true"><polyline points="2,1 6,5 2,9" fill="none" stroke="#444" stroke-width="1.6"/></svg></h4>
    <p>Sed ut perspiciatis unde omnis iste natus error sit voluptatem accusantium doloremque laudantium, totam rem aperiam, eaque ipsa quae ab illo inventore veritatis et <b>Mara Quill</b></p>
  </section>
  <section class="abs box" style="left:350px">
    <h4>NEWSLETTER</h4>
    <div class="email">Email Address</div>
    <div class="go">GO</div>
  </section>

  <div class="abs footer-line"></div>
  <nav class="abs footer-nav">
    <span>HOME</span><span>ABOUT US</span><span>SERVICES</span><span>GALLERY</span><span>BLOG</span><span>TESTIMONIALS</span><span>CONTACT US</span>
  </nav>
  <div class="abs footer-legal">
    <span>CAREERS</span><span>MEDIA</span><span>SITEMAP</span><span>LEGAL</span><span>PRIVACY POLICY</span><span>©2014 HARBOR BOLTS</span>
  </div>
  <div class="abs social" aria-label="Social links">
    <span style="background:#3b5fa0"></span>
    <span style="background:#e9609a"></span>
    <span style="background:#55c3ea"></span>
    <span style="background:#51789e"></span>
    <span style="background:#d24b3c"></span>
  </div>

</div>
</body>
</html>
```